BRV TAX & ACCOUNTING business card
Income tax, audit, bookkeeping, setup, training and services
Professional
Derek Lim Varga
48 Bexwell Drive
Toronto, ON M2K 4T8
brv_tax@quillmail.ca

```html
<!DOCTYPE html>
<html lang="en">
<head>
<meta charset="utf-8">
<title>BRV Tax &amp; Accounting – Business Card</title>
<link rel="stylesheet" href="https://fonts.googleapis.com/css2?family=Open+Sans:wght@400;600;700;800&display=swap">
<style>
  :root {
    --bg: #e9e9e6;
    --card: #ffffff;
    --green: #7cc242;
    --ink: #1f1f1f;
    --text: #333333;
    --icon: #6d6d6d;
  }
  * { margin: 0; padding: 0; box-sizing: border-box; }
  html, body {
    width: 1200px; height: 902px; overflow: hidden;
    background: var(--bg);
    font-family: "Open Sans", Arial, sans-serif;
  }
  .card {
    position: absolute; left: 100px; top: 165px;
    width: 1000px; height: 572px;
    background: var(--card);
    box-shadow: 0 6px 24px rgba(0,0,0,.18);
    overflow: hidden;
  }
  .side-band {
    position: absolute; right: 0; top: 0;
    width: 44px; height: 100%;
    background: var(--green);
  }
  .side-band__url {
    position: absolute; right: 12px; top: 22px;
    writing-mode: vertical-rl;
    color: #fff; font-size: 15px; font-weight: 600; letter-spacing: 1.5px;
  }
  .brand {
    position: absolute; left: 72px; top: 110px;
    display: flex; align-items: center; gap: 16px;
  }
  .brand__mark {
    width: 34px; height: 34px; border-radius: 50%;
    background: var(--green);
  }
  .brand__name {
    font-size: 30px; font-weight: 800; color: var(--green);
    letter-spacing: .5px;
  }
  .holder {
    position: absolute; left: 0; top: 302px;
    display: flex; align-items: center; gap: 14px;
  }
  .holder__pointer { width: 22px; height: 30px; }
  .holder__name {
    font-size: 26px; font-weight: 700; color: var(--green);
  }
  .contact {
    position: absolute; left: 575px; top: 250px;
    list-style: none;
  }
  .contact__item {
    display: flex; align-items: flex-start; gap: 12px;
    font-size: 23px; color: var(--text); line-height: 32px;
    margin-bottom: 4px;
  }
  .contact__icon {
    flex: 0 0 24px; width: 24px; height: 24px; margin-top: 4px;
  }
  .contact__lines span { display: block; }
</style>
</head>
<body>
  <main class="card">
    <div class="side-band"><span class="side-band__url">www.brvtaxpro.ca</span></div>

    <div class="brand">
      <span class="brand__mark"></span>
      <span class="brand__name">BRV TAX &amp; ACCOUNTING</span>
    </div>

    <div class="holder">
      <svg class="holder__pointer" viewBox="0 0 22 30"><polygon points="0,0 22,15 0,30" fill="var(--ink)"/></svg>
      <span class="holder__name">Derek Lim Varga</span>
    </div>

    <ul class="contact">
      <li class="contact__item">
        <svg class="contact__icon" viewBox="0 0 24 24"><circle cx="12" cy="12" r="12" fill="var(--icon)"/><path d="M5 12.5 12 6l7 6.5h-2V18h-3.5v-4h-3v4H7v-5.5z" fill="#fff"/></svg>
        <div class="contact__lines"><span>48 Bexwell Drive</span><span>Toronto, ON M2K 4T8</span></div>
      </li>
      <li class="contact__item">
        <svg class="contact__icon" viewBox="0 0 24 24"><circle cx="12" cy="12" r="12" fill="var(--icon)"/><path d="M8 6h2.5l1 3.5-1.6 1.2a8 8 0 0 0 3.4 3.4l1.2-1.6 3.5 1V16a2 2 0 0 1-2 2A11 11 0 0 1 6 8a2 2 0 0 1 2-2z" fill="#fff"/></svg>
        <div class="contact__lines"><span>416-555-014-2</span></div>
      </li>
      <li class="contact__item">
        <svg class="contact__icon" viewBox="0 0 24 24"><circle cx="12" cy="12" r="12" fill="var(--icon)"/><rect x="6" y="8" width="12" height="8.5" rx="1" fill="#fff"/><path d="M6.5 8.5 12 13l5.5-4.5" fill="none" stroke="var(--icon)" stroke-width="1.3"/></svg>
        <div class="contact__lines"><span>brv_tax@quillmail.ca</span></div>
      </li>
      <li class="contact__item">
        <svg class="contact__icon" viewBox="0 0 24 24"><circle cx="12" cy="12" r="12" fill="var(--icon)"/><g fill="none" stroke="#fff" stroke-width="1.4"><circle cx="12" cy="12" r="6.5"/><ellipse cx="12" cy="12" rx="2.8" ry="6.5"/><path d="M5.5 12h13"/></g></svg>
        <div class="contact__lines"><span>www.brvtaxpro.ca</span></div>
      </li>
    </ul>
  </main>
</body>
</html>
```